Advertisement Coaching practice

I need an advertisement (to be printed in newspaper). I have a coaching practice where I offer coaching, workshops family constellations and relationship therapy. The ad needs to express calmness, inspiration to transform but also not dull and boring. It would be great if you could use the colors from my logo into the ad.

Dimensions are: 13,04 cm Width x 9,72 cm Height.

I will add my previous self-made ad, my company logo, a portrait photo of myself and the text I want to add. Also my contact details should be visible as well.

Requirements
Nice to have
• I have updated the brief with a flyer that I had previously made by a designer. It would be a nice to have if the ad ties in with that. You can also look at my website at www.fernbrook.nu to see what colors I used there.

```html
<!DOCTYPE html>
<html lang="nl">
<head>
<meta charset="utf-8">
<title>Fernbrook – Coaching advertentie</title>
<link rel="stylesheet" href="https://fonts.googleapis.com/css2?family=Montserrat:wght@800&family=Quicksand:wght@500;600;700&display=swap">
<style>
  :root {
    --gold: #9c8232;
    --gold-dark: #7f6a25;
    --gold-light: #b39a4a;
    --navy: #1e3457;
    --white: #ffffff;
    --text: #3a3a3a;
    --logo-grey: #5e5e5e;
    --page: #e6e6e6;
  }
  * { margin: 0; padding: 0; box-sizing: border-box; }
  html, body { width: 1200px; height: 720px; overflow: hidden; background: var(--page); }
  .ad {
    position: absolute; left: 150px; top: 24px;
    width: 900px; height: 671px;
    background: var(--white);
    overflow: hidden;
    font-family: "Quicksand", sans-serif;
  }
  .ad-shapes { position: absolute; inset: 0; width: 900px; height: 671px; }
  .headline {
    position: absolute; right: 37px; top: 28px;
    font-family: "Montserrat", sans-serif; font-weight: 800;
    font-size: 38px; line-height: 48px; letter-spacing: -0.3px;
    color: var(--white); text-align: right; text-transform: uppercase;
  }
  .intro {
    position: absolute; right: 42px; top: 182px;
    font-size: 20px; line-height: 24.5px; font-weight: 500;
    color: var(--white); text-align: right; letter-spacing: 0.3px;
  }
  .intro-tab {
    position: absolute; left: 573px; top: 332px; width: 327px; height: 56px;
    background: var(--gold); border-radius: 28px 0 0 28px;
    padding-right: 37px; padding-top: 5px;
    color: var(--white); text-align: right;
    font-size: 18.5px; line-height: 23px; font-weight: 500; letter-spacing: 0.4px;
  }
  .intro-tab strong { font-weight: 700; }
  .service { position: absolute; top: 407px; width: 150px; margin-left: -75px; text-align: center; }
  .service-icon { display: block; width: 66px; height: 66px; margin: 0 auto 8px; }
  .service-label { font-size: 11px; line-height: 14.5px; font-weight: 600; color: var(--text); }
  .offer {
    position: absolute; right: 35px; top: 538px; width: 570px;
    font-size: 10.4px; line-height: 14.8px; font-weight: 500;
    color: var(--text); text-align: right;
  }
  .contact-bar {
    position: absolute; left: 286px; top: 608px; width: 614px; height: 23px;
    background: var(--gold); color: var(--white);
    font-size: 13.6px; line-height: 23px; font-weight: 500;
    padding-left: 8px; white-space: nowrap;
  }
  .contact-bar span { margin-right: 7px; }
  .brand { position: absolute; left: 47px; top: 505px; width: 200px; text-align: center; }
  .brand-mark { display: block; width: 62px; height: 62px; margin: 0 auto 8px; border: 2px solid var(--logo-grey); border-radius: 50%; }
  .brand-name { font-size: 38px; line-height: 42px; font-weight: 600; color: var(--logo-grey); }
</style>
</head>
<body>
<div class="ad">
  <svg class="ad-shapes" viewBox="0 0 1642 1224" preserveAspectRatio="none" aria-hidden="false">
    <defs>
      <linearGradient id="goldGround" x1="0" y1="0" x2="1" y2="1">
        <stop offset="0" stop-color="#a08633"/>
        <stop offset="0.5" stop-color="#8f7729"/>
        <stop offset="1" stop-color="#a68c3a"/>
      </linearGradient>
      <radialGradient id="portraitTones" cx="0.45" cy="0.45" r="0.6">
        <stop offset="0" stop-color="#b07a5c"/>
        <stop offset="0.45" stop-color="#8c6a52"/>
        <stop offset="0.75" stop-color="#b8c3d3" stop-opacity="0.8"/>
        <stop offset="1" stop-color="#9c8232" stop-opacity="0"/>
      </radialGradient>
    </defs>
    <rect width="1642" height="1224" fill="url(#goldGround)"/>
    <rect x="0" y="30" width="820" height="960" fill="url(#portraitTones)" role="img" aria-label="Portretfoto van de coach"/>
    <path d="M0,840 C60,930 180,930 300,880 C500,790 700,730 900,700 C1050,680 1120,560 1230,480 C1330,420 1450,560 1560,570 C1600,570 1630,530 1642,490 L1642,1224 L0,1224 Z" fill="var(--navy)"/>
    <path d="M0,840 C60,930 180,930 300,880 C500,790 700,730 900,700 C1050,680 1120,560 1230,480 C1330,420 1450,560 1560,570 C1600,570 1630,530 1642,490" fill="none" stroke="var(--white)" stroke-width="8"/>
    <path d="M0,870 C70,960 190,950 320,900 C520,820 720,780 920,755 C1070,735 1140,620 1240,540 C1340,470 1460,610 1570,610 C1610,610 1632,580 1642,560 L1642,1224 L0,1224 Z" fill="var(--white)"/>
  </svg>

  <h1 class="headline">Coaching,<br>Familieopstellingen<br>&amp; Relatietherapie</h1>
  <p class="intro">Trauma’s en negatieve ervaringen vormen ons en<br>blijven nog lang voelbaar. Ze kunnen groei of geluk<br>in de weg staan.</p>

  <div class="intro-tab">IK BEN <strong>AMARA</strong> EN<br>ONDERSTEUN JE BIJ HET:</div>

  <div class="service" style="left:510px">
    <svg class="service-icon" viewBox="0 0 66 66">
      <circle cx="33" cy="33" r="31" fill="none" stroke="var(--navy)" stroke-width="3"/>
      <circle cx="36" cy="27" r="13" fill="var(--navy)"/>
      <g fill="none" stroke="var(--white)" stroke-width="1.3">
        <ellipse cx="36" cy="27" rx="10" ry="4"/>
        <ellipse cx="36" cy="27" rx="10" ry="4" transform="rotate(60 36 27)"/>
        <ellipse cx="36" cy="27" rx="10" ry="4" transform="rotate(-60 36 27)"/>
      </g>
      <rect x="12" y="42" width="5" height="9" fill="var(--navy)"/>
      <path d="M18,43 h10 c4,0 6,3 10,3 l9,-3 c2,0 2,3 0,4 l-12,6 h-17 z" fill="var(--navy)"/>
    </svg>
    <p class="service-label">Doorbreken van<br>belemmerende patronen</p>
  </div>

  <div class="service" style="left:661px">
    <svg class="service-icon" viewBox="0 0 66 66">
      <circle cx="33" cy="33" r="31" fill="none" stroke="var(--navy)" stroke-width="3"/>
      <path d="M10,28 l8,-8 l10,6 l8,-4 l12,0 l8,8 l-6,8 l-14,12 c-2,2 -5,1 -5,-1 l-2,0 c-2,2 -5,1 -5,-2 l-3,-1 c-2,1 -4,-1 -3,-3 z" fill="var(--navy)"/>
      <path d="M28,30 l8,-4 l10,8 M30,38 l6,5 M26,41 l5,4" fill="none" stroke="var(--white)" stroke-width="1.5"/>
    </svg>
    <p class="service-label">Beter omgaan met<br>conflicten</p>
  </div>

  <div class="service" style="left:795px">
    <svg class="service-icon" viewBox="0 0 66 66">
      <circle cx="33" cy="33" r="31" fill="none" stroke="var(--navy)" stroke-width="3"/>
      <g stroke="var(--navy)" stroke-width="1.5" fill="none">
        <polygon points="33,13 50,23 50,43 33,53 16,43 16,23"/>
        <line x1="33" y1="13" x2="33" y2="24"/><line x1="33" y1="42" x2="33" y2="53"/>
        <line x1="16" y1="23" x2="25" y2="28"/><line x1="50" y1="23" x2="41" y2="28"/>
        <line x1="16" y1="43" x2="25" y2="38"/><line x1="50" y1="43" x2="41" y2="38"/>
      </g>
      <g fill="var(--navy)">
        <circle cx="33" cy="13" r="3"/><circle cx="50" cy="23" r="3"/><circle cx="50" cy="43" r="3"/>
        <circle cx="33" cy="53" r="3"/><circle cx="16" cy="43" r="3"/><circle cx="16" cy="23" r="3"/>
      </g>
      <circle cx="33" cy="33" r="8" fill="none" stroke="var(--navy)" stroke-width="3"/>
      <path d="M33,28 v10 M28,33 h10" stroke="var(--navy)" stroke-width="3"/>
    </svg>
    <p class="service-label">In gezonde verbinding<br>met elkaar als koppel<br>of met anderen komen</p>
  </div>

  <p class="offer">Maandelijks geef ik workshops familieopstellingen. Ook houd ik themasessies rond adoptie, moeder-dochterdynamiek of relaties. Ook bied ik individuele coaching, relatietherapie en retraites aan. Kijk op de website voor meer info of neem contact open ontdek wat het beste bij jou past.</p>

  <div class="brand">
    <span class="brand-mark"></span>
    <p class="brand-name">fernbrook</p>
  </div>

  <div class="contact-bar">
    <span>Amara Veldkamp</span>
    <span>| M: info@fernbrook.nu</span>
    <span>| T: 06-12 34 56 78 |</span>
    <span>www.fernbrook.nu</span>
  </div>
</div>
</body>
</html>
```